Wedding Marlies & Joost - Save the Date Wedding Card

I would like to have a creative save the date wedding card. We like grey/black/white colors and modern/ plain and simple.
I like the Save the Date copy big and book a flight copy smaller. I like stylish fonts for the save the date copy
Copy front:
Save the Date & book a flight
7-10-2017 Denia (Spanje)
Marlies & Joost
Onze dag is niet compleet zonder jou!
Copy back:
6-10 preferred travel date
7-10 wedding ceremony/drinks/dinner/party
8-10 hangover breakfast
Nearest Airports Valencia & Alicante
More info will be available soon!
wedding guests
Wedding

```html
<!DOCTYPE html>
<html lang="nl">
<head>
<meta charset="utf-8">
<title>Marlies &amp; Joost – Save the Date</title>
<link rel="stylesheet" href="https://fonts.googleapis.com/css2?family=Pinyon+Script&family=Great+Vibes&family=Rouge+Script&display=swap">
<style>
  :root {
    --paper: #ffffff;
    --ink: #1e1e1e;
    --ink-soft: #2c2c2c;
    --taupe: #6e6450;
    --sand: #a59a7e;
    --ornament: #d4d4d4;
    --line: #222222;
  }
  html, body {
    margin: 0;
    padding: 0;
    width: 1076px;
    height: 1200px;
    overflow: hidden;
    background: var(--paper);
  }
  .card {
    position: relative;
    width: 1076px;
    height: 1200px;
    background: var(--paper);
  }
  .frame {
    position: absolute;
    inset: 0;
  }
  .content {
    position: absolute;
    inset: 0;
    text-align: center;
  }
  .content p {
    margin: 0;
    position: absolute;
    left: 0;
    right: 0;
    line-height: 1;
  }
  .monogram {
    top: 128px;
    font-family: "Great Vibes", cursive;
    font-size: 104px;
    color: var(--taupe);
  }
  .venue {
    top: 290px;
    font-family: "Pinyon Script", cursive;
    font-size: 54px;
    color: var(--sand);
  }
  .schedule {
    font-family: "Rouge Script", cursive;
    font-size: 42px;
    color: var(--ink-soft);
  }
  .schedule-1 { top: 436px; }
  .schedule-2 { top: 498px; }
  .schedule-3 { top: 560px; }
  .schedule-4 { top: 622px; }
  .schedule-5 { top: 684px; }
  .airports {
    top: 835px;
    font-family: "Pinyon Script", cursive;
    font-size: 56px;
    color: var(--ink);
  }
  .more-info {
    top: 925px;
    font-family: "Great Vibes", cursive;
    font-size: 52px;
    color: var(--taupe);
  }
  .closing {
    top: 1048px;
    font-family: "Great Vibes", cursive;
    font-size: 30px;
    color: var(--sand);
  }
</style>
</head>
<body>
<main class="card">
  <svg class="frame" width="1076" height="1200" viewBox="0 0 1076 1200">
    <g class="frame-lines" fill="none" stroke="var(--line)">
      <rect x="72" y="74" width="932" height="1052" stroke-width="1"/>
      <rect x="86" y="88" width="904" height="1024" stroke-width="1"/>
      <line x1="310" y1="90" x2="766" y2="90" stroke-width="3"/>
      <line x1="310" y1="1110" x2="766" y2="1110" stroke-width="3"/>
      <line x1="80" y1="340" x2="80" y2="540" stroke-width="3"/>
      <line x1="80" y1="660" x2="80" y2="860" stroke-width="3"/>
      <line x1="996" y1="340" x2="996" y2="540" stroke-width="3"/>
      <line x1="996" y1="660" x2="996" y2="860" stroke-width="3"/>
    </g>
    <g class="ornaments" fill="var(--ornament)">
      <rect x="18" y="10" width="120" height="130" rx="30" role="img" aria-label="Scrolled corner ornament, top left"/>
      <rect x="938" y="10" width="120" height="130" rx="30" role="img" aria-label="Scrolled corner ornament, top right"/>
      <rect x="18" y="1060" width="120" height="130" rx="30" role="img" aria-label="Scrolled corner ornament, bottom left"/>
      <rect x="938" y="1060" width="120" height="130" rx="30" role="img" aria-label="Scrolled corner ornament, bottom right"/>
      <rect x="500" y="52" width="76" height="40" rx="16" role="img" aria-label="Scroll ornament, top centre"/>
      <rect x="500" y="1108" width="76" height="40" rx="16" role="img" aria-label="Scroll ornament, bottom centre"/>
      <rect x="22" y="555" width="52" height="90" rx="18" role="img" aria-label="Scroll ornament, left side"/>
      <rect x="1002" y="555" width="52" height="90" rx="18" role="img" aria-label="Scroll ornament, right side"/>
    </g>
  </svg>

  <section class="content">
    <p class="monogram">M&amp;J</p>
    <p class="venue">Denia Spanje</p>
    <p class="schedule schedule-1">6-10 preferred travel date</p>
    <p class="schedule schedule-2">7-10 wedding ceremony/drinks/dinner/party</p>
    <p class="schedule schedule-3">8-10 hangover lunch</p>
    <p class="schedule schedule-4">6-10 optional late lunch</p>
    <p class="schedule schedule-5">8-10 optional late breakfast</p>
    <p class="airports">Nearest Airports Valencia &amp; Alicante</p>
    <p class="more-info">More info will be available soon!</p>
    <p class="closing">Onze dag is niet compleet zonder jou!</p>
  </section>
</main>
</body>
</html>
```